Hair Extension Packaging

Update 2/16 - please keep submissions coming, I have no front runners yet. Thanks.

I need some new packaging designed for hair extensions. I have enclose pictures of what other companies packaging looks like and a few pictures of some inspiration. I am looking for a packaging that will appeal to a 20's-30's year old demographic and I like things along the lines of glamor/lace/vintage/boudoir/damask inspired. I am going to leave colors up to your creativity for the sample artwork and ask for changes if needed. Id like the design to be a standout but not loud.

The working name for this hair is "Vexa"
Additional Text that I would like on the packaging "100% Premium Virgin Remy Human Hair"

Please keep in mind that the background of the packaging will have many different colors laying over it so be mindful of what the color you chose can effect the hair color in the packaging - no red or orange which can make the hair appear very warm and clash with ashy colors.

Working dimensions for the sample are 22" long, 3" wide.

****Once I decide on the front of the packaging I will also need the back designed which will consist of similar design as the front but with hair care instructions printed on it.***** This finished product must include front and back artwork, open Photoshop files, and additional bleed room for printing. I don't want to waste anyone's time so once I get a front design I like I will work with that artist to create the back.

Please message me with any questions.
Updates

Project Deadline Extended
Reason: Finalizing final choices. Thanks for your submissions!

Target Market(s)

Women in there 20"s - 30's. High fashion, luxurious, glamour

Industry/Entity Type

Hair

Font styles to use
Serif
Script

Requirements
Must have
• Id love the product name to be in script and then mixed with regular font (see the makeup logo example I enclosed)
Should not have
• Should not be masculine. Forget the blue and green colors

```html
<!DOCTYPE html>
<html lang="en">
<head>
<meta charset="utf-8">
<title>Vexa Hair Extension Packaging</title>
<link href="https://fonts.googleapis.com/css2?family=Gwendolyn:wght@700&family=Play:wght@700&display=swap" rel="stylesheet">
<style>
  :root {
    --page: #ffffff;
    --tan-light: #f6ece0;
    --tan-mid: #dcc6a9;
    --tan-deep: #c4a886;
    --ink: #3a2418;
    --strip-top: #b8b0b0;
    --strip-mid: #a99aa6;
    --strip-core: #9c8496;
    --strip-low: #bcb1ad;
  }
  html, body {
    margin: 0;
    padding: 0;
    width: 1200px;
    height: 900px;
    overflow: hidden;
    background: var(--page);
  }
  .canvas {
    position: relative;
    width: 1200px;
    height: 900px;
  }
  .package {
    position: absolute;
    top: 44px;
    width: 133px;
    height: 852px;
  }
  .package__strip {
    position: absolute;
    left: 10px;
    top: 132px;
    width: 113px;
    height: 720px;
    background: linear-gradient(to bottom,
      var(--strip-top) 0%,
      var(--strip-mid) 25%,
      var(--strip-core) 40%,
      var(--strip-mid) 55%,
      var(--strip-low) 72%,
      var(--tan-mid) 84%,
      var(--tan-deep) 100%);
    box-shadow: 0 0 2px rgba(0,0,0,0.35);
  }
  .package__foot {
    position: absolute;
    left: 0;
    bottom: 0;
    width: 100%;
    height: 95px;
    background: linear-gradient(to bottom, rgba(220,198,169,0) 0%, var(--tan-mid) 40%, var(--tan-deep) 100%);
  }
  .package__hair {
    position: absolute;
    left: 24px;
    top: 0;
    width: 64px;
    height: 578px;
    clip-path: polygon(14% 0, 86% 0, 96% 40%, 94% 85%, 80% 100%, 20% 100%, 4% 88%, 6% 40%);
  }
  .hair--brown  { background: linear-gradient(to right, #5a3a22, #9a6a44, #6b4529, #a87a52, #5c3b22); }
  .hair--berry  { background: linear-gradient(to right, #4a0f24, #a02e55, #6b1535, #b24667, #511026); }
  .hair--violet { background: linear-gradient(to right, #4b1560, #a23fc7, #6a1f8a, #b458d6, #521868); }
  .hair--red    { background: linear-gradient(to right, #6e0a0a, #d62a1c, #8f1210, #e23a24, #7a0c0c); }

  .label {
    position: absolute;
    background: radial-gradient(ellipse at 50% 30%, var(--tan-light) 0%, var(--tan-mid) 60%, var(--tan-deep) 100%);
    box-shadow: 0 1px 3px rgba(0,0,0,0.45);
    color: var(--ink);
  }
  .label__name,
  .label__line1,
  .label__line2 {
    position: absolute;
    left: 0;
    right: 0;
    text-align: center;
    white-space: nowrap;
    line-height: 1;
  }
  .label__name {
    font-family: "Gwendolyn", cursive;
    font-weight: 700;
  }
  .label__line1,
  .label__line2 {
    font-family: "Play", sans-serif;
    font-weight: 700;
  }
  .label--tag {
    left: 0;
    top: 0;
    width: 133px;
    height: 132px;
  }
  .label--tag .label__name  { top: 8px;  font-size: 44px; }
  .label--tag .label__line1 { top: 99px; font-size: 9.5px; }
  .label--tag .label__line2 { top: 111px; font-size: 8.5px; }

  .label--hero {
    left: 808px;
    top: 270px;
    width: 350px;
    height: 350px;
  }
  .label--hero .label__name  { top: 30px;  font-size: 130px; }
  .label--hero .label__line1 { top: 266px; font-size: 24px; letter-spacing: 1px; }
  .label--hero .label__line2 { top: 297px; font-size: 21px; letter-spacing: 1px; }
</style>
</head>
<body>
<main class="canvas">

  <section class="package" style="left:80px">
    <div class="package__strip">
      <div class="package__hair hair--brown" role="img" aria-label="Straight light brown hair extension bundle"></div>
      <div class="package__foot" role="img" aria-label="Tan panel with vintage scroll flourish"></div>
    </div>
    <div class="label label--tag">
      <div class="label__name">Vexa</div>
      <div class="label__line1">100% Premium</div>
      <div class="label__line2">Virgin Remy Human Hair</div>
    </div>
  </section>

  <section class="package" style="left:260px">
    <div class="package__strip">
      <div class="package__hair hair--berry" role="img" aria-label="Straight burgundy pink hair extension bundle"></div>
      <div class="package__foot" role="img" aria-label="Tan panel with vintage scroll flourish"></div>
    </div>
    <div class="label label--tag">
      <div class="label__name">Vexa</div>
      <div class="label__line1">100% Premium</div>
      <div class="label__line2">Virgin Remy Human Hair</div>
    </div>
  </section>

  <section class="package" style="left:440px">
    <div class="package__strip">
      <div class="package__hair hair--violet" role="img" aria-label="Straight violet hair extension bundle"></div>
      <div class="package__foot" role="img" aria-label="Tan panel with vintage scroll flourish"></div>
    </div>
    <div class="label label--tag">
      <div class="label__name">Vexa</div>
      <div class="label__line1">100% Premium</div>
      <div class="label__line2">Virgin Remy Human Hair</div>
    </div>
  </section>

  <section class="package" style="left:620px">
    <div class="package__strip">
      <div class="package__hair hair--red" role="img" aria-label="Straight bright red hair extension bundle"></div>
      <div class="package__foot" role="img" aria-label="Tan panel with vintage scroll flourish"></div>
    </div>
    <div class="label label--tag">
      <div class="label__name">Vexa</div>
      <div class="label__line1">100% Premium</div>
      <div class="label__line2">Virgin Remy Human Hair</div>
    </div>
  </section>

  <section class="label label--hero" role="img" aria-label="Header label with vintage damask swirls behind the product name">
    <div class="label__name">Vexa</div>
    <div class="label__line1">100% Premium</div>
    <div class="label__line2">Virgin Remy Human Hair</div>
  </section>

</main>
</body>
</html>
```